KMR Info Brochure

We need a brochure design for a new not-for-profit organisation that is aimed at providing homeless people with a residence that also provides counselling and vocational training to assist them to find suitable employment at the end of the program.
PLEASE NOTE:
Brochure to be A4.
I know the brochure is quite long, it is really a booklet, but please note that it does not have to have a lot of work done on it, I just want it to look professional and the front cover and inside page to look good.
Also please leave about 2-3 pages at the end as I will be adding in some architect drawings.
Please add in a last page with Contact written at the bottom - we will fill that in later. So please ensure it is editable in PDF.
Thank you so much.
Cheers
Petra

```html
<!DOCTYPE html>
<html lang="en">
<head>
<meta charset="utf-8">
<title>KMR Legacy Foundation – Info Brochure Spreads</title>
<link href="https://fonts.googleapis.com/css2?family=Marcellus&family=Open+Sans:wght@400;600;700&display=swap" rel="stylesheet">
<style>
:root{
  --stage:#3a2a20;
  --label:#f2f2f2;
  --blue:#1b57ab;
  --blue-dark:#0e3f8a;
  --blue-light:#5a93d6;
  --ink:#4a4a4a;
  --muted:#8a8a8a;
  --paper:#ffffff;
  --gold:#c9a227;
  --green:#7a8f2a;
}
*{box-sizing:border-box;margin:0;padding:0}
html,body{width:1200px;height:863px;overflow:hidden;background:var(--stage)}
body{position:relative;font-family:"Open Sans",Arial,sans-serif;color:var(--ink)}
.label{position:absolute;color:var(--label);font:700 12px "Open Sans",Arial,sans-serif}
.spread{position:absolute;display:flex;box-shadow:0 3px 10px rgba(0,0,0,.45)}
.page{position:relative;width:264px;background:var(--paper);overflow:hidden}
.spread-top .page{height:288px;background:transparent}
.spread-bottom .page{height:353px}
.spread-bg{position:absolute;left:0;top:0;width:528px;height:288px;background:var(--paper)}
.spread-bg > div{position:absolute}
.gutter{left:263px;top:0;width:1px;height:288px;background:rgba(0,0,0,.08)}

/* cover */
.cover-blue{left:0;top:0;width:528px;height:200px;background:linear-gradient(180deg,#1f5db3,#164c9c)}
.wave-placeholder{left:0;top:200px;width:528px;height:54px;background:linear-gradient(180deg,#164c9c 0%,#6e9fdc 55%,#ffffff 100%)}

/* page 2 / contents */
.inner-blue{left:0;top:0;width:240px;height:288px;background:linear-gradient(135deg,#1a55a8,#2f6fc0)}
.swoosh-placeholder{left:240px;top:0;width:22px;height:288px;background:linear-gradient(90deg,#2f6fc0,#9fc1e8 60%,#ffffff)}
.edge-placeholder{left:506px;top:0;width:22px;height:288px;background:linear-gradient(90deg,#ffffff,#dfe3e8 60%,#c7c7c7)}

.cover-title{position:absolute;font-family:"Marcellus",Georgia,serif;color:#fff;line-height:1.2;letter-spacing:.5px}
.cover-title .line1{font-size:17px}
.cover-title .line2{font-size:15px}
.brand{position:absolute;display:flex;align-items:center;gap:5px;font-family:"Open Sans",Arial,sans-serif;font-weight:700;color:var(--gold);white-space:nowrap}
.brand .dot{border-radius:50%;background:var(--green)}
.brand-lg{font-size:12px}
.brand-lg .dot{width:14px;height:14px}
.brand-sm{font-size:6px}
.brand-sm .dot{width:8px;height:8px}
.contact{position:absolute;font-size:3.6px;line-height:1.5;color:var(--ink)}
.contact strong{font-weight:700}

.contents-title{position:absolute;left:18px;top:28px;font:700 15px "Open Sans",Arial,sans-serif;color:var(--blue)}
.toc{position:absolute;left:18px;top:56px;width:190px;font-size:3.6px;line-height:5.05px;color:var(--ink)}
.toc li{list-style:none;display:flex;justify-content:space-between;padding:0 3px 0 9px}
.toc li.sec{background:var(--blue);color:#fff;font-weight:700;padding-left:3px;margin-top:2px}
.toc li.sec.first{background:var(--blue-dark)}
.toc li.sub2{padding-left:16px}
.toc li.att{color:var(--blue);padding-left:3px;margin-top:2px}

/* inner pages */
.top-strip{position:absolute;left:0;top:0;width:100%;height:7px;background:var(--blue)}
.col{position:absolute;top:24px;font-size:3.7px;line-height:1.55;color:var(--ink)}
.col p{margin-bottom:5px}
.col h2{font-size:6px;color:var(--blue);font-weight:700;margin-bottom:7px}
.col h3{font-size:4.2px;color:var(--blue-dark);font-weight:700;margin:6px 0 4px 8px}
.checks{display:grid;grid-template-columns:1fr 1fr;column-gap:6px;row-gap:1px;margin:4px 0 7px}
.checks li{list-style:none;display:flex;align-items:center;gap:3px}
.checks li::before{content:"";width:4px;height:4px;background:var(--blue);flex:none}
.checks li:empty::before{display:none}
.numbered li{list-style:none;margin:0 0 4px 8px}
.footnotes{position:absolute;left:20px;bottom:32px;width:200px;font-size:2.8px;line-height:1.5;color:var(--blue)}
.footer-bar{position:absolute;bottom:10px;height:6px;background:var(--blue);color:#fff;font-size:3.6px;line-height:6px}
.footer-bar.left{left:0;width:190px;padding-left:18px}
.footer-bar.right{right:0;width:128px;text-align:right;padding-right:18px}
.footer-brand-left{position:absolute;bottom:9px;right:14px}
.footer-brand-right{position:absolute;bottom:9px;left:14px}
</style>
</head>
<body>

<div class="label" style="left:64px;top:26px">BACK Page</div>
<div class="label" style="left:517px;top:26px">FRONT Page1</div>
<div class="label" style="left:627px;top:4px">Page 2</div>
<div class="label" style="left:1070px;top:4px">Content Page 3</div>
<div class="label" style="left:62px;top:815px">Page 4</div>
<div class="label" style="left:545px;top:819px">Page 5</div>
<div class="label" style="left:617px;top:815px">Page 6</div>
<div class="label" style="left:1100px;top:819px">Page 7</div>

<!-- back & front cover -->
<section class="spread spread-top" style="left:60px;top:47px">
  <div class="spread-bg">
    <div class="cover-blue"></div>
    <div class="wave-placeholder" role="img" aria-label="Flowing blue wave decoration across the cover"></div>
    <div class="gutter"></div>
  </div>
  <div class="page">
    <div class="brand brand-sm" style="left:12px;top:258px"><span class="dot"></span>KMR</div>
    <div class="contact" style="left:54px;top:255px">
      <strong>KMR Legacy Foundation</strong><br>
      Suite 000, Hillsdale, Country name<br>
      <strong>Tel:</strong> (02) 9555 0148 &nbsp;<strong>Email:</strong> info@kmrlegacy.org<br>
      <strong>www.kmrlegacy.org</strong>
    </div>
  </div>
  <div class="page">
    <div class="cover-title" style="left:56px;top:40px">
      <div class="line1">KMR LEGACY</div>
      <div class="line2">FOUNDATION</div>
    </div>
    <div class="brand brand-lg" style="left:88px;top:256px"><span class="dot"></span>KMR Legacy Foundation</div>
  </div>
</section>

<!-- page 2 & contents -->
<section class="spread spread-top" style="left:617px;top:47px">
  <div class="spread-bg">
    <div class="inner-blue"></div>
    <div class="swoosh-placeholder" role="img" aria-label="Curved blue and white swoosh decoration along the page edge"></div>
    <div class="edge-placeholder" role="img" aria-label="Grey and blue swoosh decoration at the right edge"></div>
    <div class="gutter"></div>
  </div>
  <div class="page">
    <div class="cover-title" style="left:58px;top:200px">
      <div class="line1">KMR LEGACY</div>
      <div class="line2">FOUNDATION</div>
    </div>
  </div>
  <div class="page">
    <h1 class="contents-title">Contents</h1>
    <ul class="toc">
      <li class="sec first"><span>Executive Summary</span><span>5</span></li>
      <li class="sec"><span>1. HOMELESSNESS</span><span>6</span></li>
      <li class="sec"><span>2. PROGRAM OVERVIEW</span><span>7</span></li>
      <li><span>2.1 Physiological</span><span>7</span></li>
      <li><span>2.2 Psychological</span><span>7</span></li>
      <li><span>2.3 Learning/Training</span><span>7</span></li>
      <li><span>2.4 Special Needs</span><span>8</span></li>
      <li><span>2.5 Vocational Education</span><span>8</span></li>
      <li><span>2.6 Fitting back into Society</span><span>8</span></li>
      <li><span>2.7 Outreach / After Care Program</span><span>8</span></li>
      <li><span>2.8 Family Groups</span><span>9</span></li>
      <li><span>2.9 Young People</span><span>9</span></li>
      <li><span>2.10 Older People</span><span>9</span></li>
      <li><span>2.11 Alcohol &amp; Drug Dependencies</span><span>10</span></li>
      <li class="sec"><span>3. OPERATIONS</span><span>11</span></li>
      <li><span>3.1 Management</span><span>11</span></li>
      <li><span>3.2 Business Location</span><span>11</span></li>
      <li><span>3.3 Foundation Management</span><span>11</span></li>
      <li><span>3.4 KMR Staff</span><span>12</span></li>
      <li><span>3.5 Self-Sustainment</span><span>12</span></li>
      <li><span>3.6 Timeframes</span><span>13</span></li>
      <li><span>3.7 Marketing and Publicity</span><span>13</span></li>
      <li class="sec"><span>4. THE PROGRAM PRACTICALLY</span><span>14</span></li>
      <li><span>4.1 Work Task</span><span>15</span></li>
      <li><span>4.2 Snapshot of a day in the Program</span><span>16</span></li>
      <li><span>4.3 Logistics</span><span>16</span></li>
      <li class="sec"><span>5. THE FUTURE</span><span>17</span></li>
      <li><span>5.1 Complementary Businesses</span><span>17</span></li>
      <li class="sub2"><span>5.1.1. Phase 1</span><span>17</span></li>
      <li class="sub2"><span>5.1.2. Phase 2</span><span>18</span></li>
      <li class="sub2"><span>5.1.3. Phase 3</span><span>18</span></li>
      <li class="sub2"><span>5.1.4. Phase 4</span><span>18</span></li>
      <li class="sub2"><span>5.1.5. Phase 5</span><span>19</span></li>
      <li><span>5.2 The Long Term</span><span>19</span></li>
      <li class="sec"><span>6. THE FINANCES</span><span>20</span></li>
      <li><span>6.1 Funding</span><span>20</span></li>
      <li><span>6.2 Income</span><span>20</span></li>
      <li><span>6.3 Fundraising</span><span>21</span></li>
      <li class="att"><span>Attachment 1: S.W.O.T. analysis</span><span>22</span></li>
      <li class="att" style="margin-top:0"><span>Attachment 2: Learning for Residents</span><span>23</span></li>
    </ul>
  </div>
</section>

<!-- pages 4 & 5 -->
<section class="spread spread-bottom" style="left:60px;top:437px">
  <article class="page">
    <div class="top-strip"></div>
    <div class="col" style="left:20px;width:226px">
      <h2>Executive Summary</h2>
      <p>KMR Legacy Foundation (KMRLF) is a not-for-profit organisation that will attempt to break the cycle of homelessness. KMR will provide a live-in residence for homeless people from all age ranges and provide psychological counselling to address the issues associated with the reasons for, and impact of, homelessness.</p>
      <p>It is expected that each Resident will remain on average twelve months in residence to address their psychological issues. During this time the Resident will also be provided with various types of training, from life skills to specific vocational education, to assist them to move towards independent living.</p>
      <p>Once the Resident is ready, KMR staff will assist the Resident with all aspects of transitioning to independent living and provide on-going assistance and support for as long as is required.</p>
      <p>KMR will cater for family groups and single parents, providing counselling for the entire family group and training for the parent. During the residency the children will attend a local school to reduce the impact to their education.</p>
      <p>KMR recognises that the cost of running the facility and providing training and work experience to a reasonably large group of people in today's economic environment will be challenging. As such, KMR is working towards establishing complementary business entities that will provide the necessary training and income for the Residents.</p>
      <p>Overall, KMR aims to reduce the overall incidence of homelessness Australia wide.</p>
      <p style="margin-top:22px">Residents = homeless people living at KMR complex.</p>
      <p>Clients = Residents who have been through the Program and returned to independent living, but remain in the After Care program.</p>
    </div>
    <div class="footer-bar left">4</div>
    <div class="brand brand-sm footer-brand-left"><span class="dot"></span>KMR</div>
  </article>
  <article class="page">
    <div class="top-strip"></div>
    <div class="col" style="left:18px;width:226px">
      <h2>1. Homelessness</h2>
      <p>Numerous national, state and local reports repeatedly indicate that there is not one single cause that leads to homelessness. However, without the financial ability to make ends meet and afford a home, individuals and families become homeless. Other factors that contribute to homelessness include:</p>
      <ul class="checks">
        <li>Poverty</li><li>Unemployment</li>
        <li>Lack of affordable housing</li><li>Poor physical or mental health</li>
        <li>Drug and alcohol abuse</li><li>Gambling</li>
        <li>Family and relationship breakdown</li><li>Domestic violence</li>
        <li>Physical and/or sexual abuse</li><li></li>
      </ul>
      <p>There are currently 105,237 people in Australia who are homeless. The rate of homelessness is 49 out of every 10,000 people (0.5% of the population). There are approximately 56% men and 44% female. The age breakdown is as follows:</p>
      <ul class="checks">
        <li>Under 12: 17% (17,845)</li><li>12–18: 10% (10,313)</li>
        <li>19–24: 15% (15,325)</li><li>25–34: 16% (16,707)</li>
        <li>35–44: 14% (14,494)</li><li>45–54: 12% (12,531)</li>
        <li>55–64: 8% (8,665)</li><li>65–74: 4% (4,174)</li>
        <li>75 and over: 3% (3,036)</li><li></li>
      </ul>
      <p>Due to the wide spread of demographics of homeless people, KMR will cater for all age ranges and sexes, as well as family groups. The target market for KMR will be anyone that is homeless. Secondary placement consideration will also be given to anyone else on a case-by-case basis. The current homeless statistics are as follows:</p>
      <ul class="checks">
        <li>NSW: 28,190 (40.8 per 10,000)</li><li>VIC: 22,789 (42.4 per 10,000)</li>
        <li>QLD: 19,838 (45.8 per 10,000)</li><li>SA: 5,985 (37.5 per 10,000)</li>
        <li>WA: 9,592 (42.3 per 10,000)</li><li>TAS: 1,579 (31.9 per 10,000)</li>
        <li>NT: 15,479 (730.7 per 10,000)</li><li>ACT: 1,785 (50 per 10,000)</li>
      </ul>
    </div>
    <div class="footnotes">
      ¹ Homelessness statistics, national census report, 2011<br>
      ² Counting the homeless, state summary tables, 2011<br>
      ³ Estimating homelessness, population and housing figures
    </div>
    <div class="footer-bar right">5</div>
    <div class="brand brand-sm footer-brand-right"><span class="dot"></span>KMR</div>
  </article>
</section>

<!-- pages 6 & 7 -->
<section class="spread spread-bottom" style="left:617px;top:437px">
  <article class="page">
    <div class="top-strip"></div>
    <div class="col" style="left:20px;width:226px">
      <h2>2. Program Overview</h2>
      <p>KMR Legacy Foundation (KMRLF) aims to provide homeless people (Residents) with the tools necessary to re-enter society as functional, productive and balanced members of society. KMR aims to assist homeless people, not by just giving them a shelter, but by addressing the initial cause of homelessness and providing the tools necessary to gain independent living, and so stop the cycle.</p>
      <p>KMR will house Residents in a residential facility; while they are at the facility they will receive physiological and psychological care, assistance with basic and skilled training and vocational education. Once the Residents have completed their program, KMR will assist them to fit back into society, find a job and housing.</p>
      <h3>2.1. &nbsp;Physiological</h3>
      <p>Our bodies and mind suffer when exposed to poor nutrition and lack of sleep. Homeless people are at greater risk of chronic health problems and many do not have access to regular medical care or a general practitioner.</p>
      <p>As part of the intake process, KMR will do a complete medical assessment of each Resident to assess their level of wellness.</p>
      <h3>2.2. &nbsp;Psychological</h3>
      <p>A majority of Residents will experience some form of anxiety, depression or post-traumatic stress disorder. Therefore it will be a requirement for all Residents to undertake counselling sessions throughout their stay at KMR.</p>
      <p>At the initial intake process a full psychological analysis will be undertaken and a specific program will be developed for each Resident.</p>
      <h3>2.3. &nbsp;Learning/Training</h3>
      <p>Life skills are the skills that many people take for granted, like managing money, shopping, cooking and cleaning. Some homeless people do not have all of these skills, either because they never acquired them or because they lost them through extended periods of homelessness.</p>
      <p>Life skills can be thought of in terms of four broad categories:</p>
      <ol class="numbered">
        <li>1) &nbsp;Core or basic skills (literacy, numeracy and information technology)</li>
        <li>2) &nbsp;Independent living skills (eg. finance, nutrition, employment)</li>
      </ol>
    </div>
    <div class="footer-bar left">6</div>
    <div class="brand brand-sm footer-brand-left"><span class="dot"></span>KMR</div>
  </article>
  <article class="page">
    <div class="top-strip"></div>
    <div class="col" style="left:18px;width:226px">
      <ol class="numbered">
        <li>3) &nbsp;Social skills (eg. interpersonal skills, conflict resolution, developing self-confidence and social networks)</li>
        <li>4) &nbsp;Tenancy requirements (eg. letting agreements, rent)</li>
      </ol>
      <p>It is anticipated that most Residents will need to undertake some aspect of Life Skills, which will be assessed during the initial intake phase.</p>
      <h3>2.4. &nbsp;Special Needs</h3>
      <p>According to one study, the number of homeless youth diagnosed with learning disabilities is double the rate of other children. KMR plans to work one on one with Residents with learning disabilities to assist them to complete their education.</p>
      <h3>2.5. &nbsp;Vocational Education</h3>
      <p>Vocational education is education that prepares people for specific trades, crafts and careers at various levels. KMR will offer vocational training matched to each Resident's skills, interests and abilities.</p>
      <p>KMR will do everything in its power to assist each Resident to achieve their desired outcomes, as vocational skills training is the cornerstone of Residents moving into independent living options.</p>
      <h3>2.6. &nbsp;Fitting back into Society</h3>
      <p>Once the Residents are ready to fit back into Society, KMR will assist them every step of the way. The Residents Caseworker will step them through all aspects of independent living including:</p>
      <ul class="checks">
        <li>Appropriate Employment</li><li>Housing / tenancy agreements</li>
        <li>Connecting utilities</li><li>Furnishing</li>
        <li>Transportation</li><li>Schools</li>
        <li>Churches</li><li>Outstanding debts</li>
      </ul>
      <h3>2.7. &nbsp;Outreach / After Care Program</h3>
      <p>Once a Resident has finished the internal program, they will be transitioned over a period of time to become a Client. The Client will be assisted to fit back into society, and visited at regular intervals to ensure they have every chance of success.</p>
    </div>
    <div class="footnotes">¹ Source: Youth and learning disability report, national study, 2010</div>
    <div class="footer-bar right">7</div>
    <div class="brand brand-sm footer-brand-right"><span class="dot"></span>KMR</div>
  </article>
</section>

</body>
</html>
```